Etiketten-Design für nachhaltige Rasur- & Pflegeprodukte
> Wir suchen Verpackung und Etiketten für eine Marke für nachhaltige Rasur- & Pflegeprodukte.
Habedere liebe Designer,
„Habedere“ sagt man bei uns in Bayern, es bedeutet Hallo oder auf Wiedersehen, je nach Gelegenheit. In diesem Fall: Hallo.
Vielleicht kennst du uns schon, wir sind greenpines, wir betreiben einen kleinen Shop für Bartpflege & Rasur unter greenpines-shop.de und wir versuchen uns nun an einem neuen Thema: nachhaltige Rasur- & Pflegeprodukte für Frauen.
Das machen wir unter dem Namen „Sanft“.
Weil die Frage schon oft aufkam: Jawohl, wir haben uns dafür die Beine und die Achseln mit einem Rasierhobel rasiert.
> Zielgruppe.
Wir arbeiten an einer neuen Pflegelinie für Frauen, die sich vorwiegend mit der Rasur und den dazugehörigen Pflegeprodukten beschäftigt. Die Zielgruppe sind vor allem online-affine Frauen aus Deutschland, Österreich und der Schweiz, aber sicher auch europaweit im Alter von 21-45.
> Aufgabenstellung.
Wir sind auf der Suche nach einem Konzept für unsere Produktverpackungen bzw. Etiketten. Bei den Pflegeprodukten verzichten wir bewusst auf eine Umverpackung.
Konkret geplant sind ein Rasierhobel, dafür haben wir eine schöne Umverpackung. Außerdem starten wir mit Rasieröl, Rasierseife und einem After Shave Balsam. Es werden später noch andere Artikel dazukommen, eine Deocreme zum Beispiel.
Rasieröl, Rasiercreme und After Shave Balsam duften nach Orangen, es werden zwei oder drei weitere Duftrichtungen folgen, die eine wird beispielsweise nach Beeren duften, die andere nach Pfirsich und Mango – bitte beachte das bei der Erstellung des Konzeptes, die Unterschiede sollten später auf den ersten Blick erkennbar sein.
Zurück zum Thema Orange: Wir würden den Duft als leicht herben Zitrusduft bezeichnen.
> Die Maße.
• Umverpackung Rasierhobel, weißer Karton (165x90x40mm)
• Rasieröl 30ml (Etikett: 100x46mm)
• Rasiercreme 60ml (Etikett: 156x32mm)
• After Shave Balsam 60ml (Etikett: 156x32mm)
> Zwingend erforderliche Angaben.
Da es sich um Kosmetikprodukte handelt, sind einige Angaben auf dem Label zwingend erforderlich, beispielhaft sollen die folgenden Infos als Platzhalter dienen.
• Hergestellt für Tobias Kranzler e.K. von greenpines, Lindenhofweg 27, 83109 Rosenheim
• Ingredients: Aqua, Stearic Acid, Cocos Nucifera oil, Glycerin, Potassium Hydroxide, Litsea Cubeba oil, (and) Citrus Sinensis Peel oil, Orbignya Oleifera oil, Sodium Hydroxide, Macadamia ternifolia oil, Talc, Kaolin, Citric Acid, Simmondsia chinensis oil, Maris sal, C.I. 77892 (and) Rad Clay, Citral, Limonene, Linalool, Geraniol
• Platz für einen Barcode
• Rasieröl sind 30ml / 1.01 FL.OZ. ODER Creme & Balsam jeweils 60ml / 2.03 FL. OZ.
Wir haben ein Bild der aktuellen Gefäße beigefügt, es kann aber durchaus sein, dass wir uns noch umen..

```html
<!DOCTYPE html>
<html lang="de">
<head>
<meta charset="utf-8">
<title>Sanft – Rasieröl Etikett &amp; Rasierhobel Verpackung</title>
<link href="https://fonts.googleapis.com/css2?family=Playfair+Display:wght@800&family=Courier+Prime&family=Montserrat:wght@300;500;700&display=swap" rel="stylesheet">
<style>
  :root {
    --backdrop: #dcdcdc;
    --orange: #e2a764;
    --orange-text: #d99a52;
    --label-white: #f1efec;
    --box-paper: #ebe8e4;
    --sage: #8aa49e;
    --leaf: #cfd6d2;
    --ink: #2f2f2f;
    --ink-soft: #6a6a6a;
  }
  * { margin: 0; padding: 0; box-sizing: border-box; }
  html, body {
    width: 1200px; height: 900px; overflow: hidden;
    background: var(--backdrop);
  }
  .stage {
    position: relative; width: 1200px; height: 900px;
    display: flex; align-items: center; justify-content: center; gap: 110px;
  }

  /* Rasieröl label */
  .oil-label {
    position: relative; width: 360px; height: 420px;
    background: var(--label-white);
    overflow: hidden;
  }
  .oil-label__band {
    position: absolute; left: 0; top: 0; width: 100%; height: 260px;
  }
  .oil-label__mark {
    position: absolute; left: 50%; top: 50px; transform: translateX(-50%);
    width: 140px; height: 140px; border-radius: 50%;
    background: var(--label-white);
    display: flex; align-items: center; justify-content: center;
    font-family: "Montserrat", sans-serif; font-weight: 300;
    font-size: 30px; color: var(--orange-text); letter-spacing: 1px;
  }
  .oil-label__blossom {
    position: absolute; right: 18px; top: 270px;
    width: 110px; height: 120px; border-radius: 50%;
    background: radial-gradient(circle, #f3e3cf 0%, #f1efec 75%);
  }
  .oil-label__text {
    position: absolute; left: 0; top: 278px; width: 100%;
    text-align: center; color: var(--orange-text);
  }
  .oil-label__product {
    font-family: "Playfair Display", serif; font-weight: 800; font-size: 24px;
  }
  .oil-label__scent {
    font-family: "Courier Prime", monospace; font-size: 21px; margin-top: 2px;
  }
  .oil-label__origin {
    font-family: "Courier Prime", monospace; font-size: 11px; font-style: italic;
    margin-top: 30px; letter-spacing: 1px;
  }
  .oil-label__volume {
    font-family: "Courier Prime", monospace; font-size: 11px; margin-top: 2px;
  }

  /* Rasierhobel box front */
  .razor-box {
    position: relative; width: 330px; height: 605px;
    background: var(--box-paper);
    overflow: hidden;
  }
  .razor-box__leaf {
    position: absolute; left: 70px; top: 190px; width: 250px; height: 330px;
    background: linear-gradient(160deg, #d6dcd8 0%, var(--leaf) 100%);
    border-radius: 60% 10% 60% 10%;
    opacity: .8;
  }
  .razor-box__mark {
    position: absolute; left: 30px; top: 60px;
    width: 250px; height: 250px; border-radius: 50%;
    background: var(--sage);
    display: flex; align-items: center; justify-content: center;
    font-family: "Montserrat", sans-serif; font-weight: 300;
    font-size: 52px; color: #eef0ee; letter-spacing: 2px;
  }
  .razor-box__title {
    position: absolute; left: 34px; top: 385px;
    font-family: "Montserrat", sans-serif; color: var(--ink);
  }
  .razor-box__product { font-weight: 700; font-size: 22px; letter-spacing: .5px; }
  .razor-box__variant { font-weight: 300; font-size: 22px; color: var(--ink-soft); letter-spacing: .5px; }
  .razor-box__audience {
    position: absolute; left: 34px; bottom: 48px;
    font-family: "Montserrat", sans-serif; font-weight: 500;
    font-size: 11px; color: var(--ink); letter-spacing: .5px;
  }
</style>
</head>
<body>
<main class="stage">

  <section class="oil-label" aria-label="Etikett Rasieröl Orange Blossom">
    <svg class="oil-label__band" viewBox="0 0 360 260" preserveAspectRatio="none" aria-hidden="true">
      <path d="M0 0 H360 V238 C300 232 250 250 190 244 C130 238 70 258 0 250 Z" fill="var(--orange)"/>
    </svg>
    <div class="oil-label__mark">Sanft</div>
    <div class="oil-label__blossom" role="img" aria-label="Feine Linienzeichnung einer Orangenblüte"></div>
    <div class="oil-label__text">
      <p class="oil-label__product">Rasieröl</p>
      <p class="oil-label__scent">Orange Blossom</p>
      <p class="oil-label__origin">handmade in germany</p>
      <p class="oil-label__volume">30ml / 1.01 FL.OZ.</p>
    </div>
  </section>

  <section class="razor-box" aria-label="Verpackung Rasierhobel">
    <div class="razor-box__leaf" role="img" aria-label="Große, blasse Blattillustration im Hintergrund"></div>
    <div class="razor-box__mark">Sanft</div>
    <div class="razor-box__title">
      <p class="razor-box__product">RASIERHOBEL</p>
      <p class="razor-box__variant">EXTRA SANFT</p>
    </div>
    <p class="razor-box__audience">RASIERER FÜR FRAUEN</p>
  </section>

</main>
</body>
</html>
```